Flyer-Design für psychologische Beratungspraxis für Mütter
Zielgruppe
Gelassenheitswerkstatt ist eine psychologische Beratungspraxis. Ich unterstütze Mütter, Schwangere und Frauen mit Kinderwunsch bei Herausforderungen rund um Schwangerschaft, Geburt, Mutterschaft, und damit einhergehenden Problemen.
Aufgabenstellung
Text nochmal geringgradig geändert...siehe Datei anbei

```html
<!DOCTYPE html>
<html lang="de">
<head>
<meta charset="utf-8">
<title>Gelassenheitswerkstatt – Flyer</title>
<link href="https://fonts.googleapis.com/css2?family=Archivo:wght@400;600;700;800&display=swap" rel="stylesheet">
<style>
  :root{
    --ink:#2c2f8c;
    --ink-soft:#5a5fb0;
    --page-tint:#e2e6e3;
    --page-white:#f8f8f6;
    --backdrop:#e9e8e5;
    --pill:#e9e9ef;
    --photo-sky:#a9bfd0;
    --photo-hair:#c8a77f;
    --photo-skin:#d9b2a0;
    --photo-grey:#9aa3b3;
  }
  *{box-sizing:border-box;margin:0;padding:0}
  html,body{width:1200px;height:864px;overflow:hidden}
  body{background:var(--backdrop);font-family:"Archivo",Arial,sans-serif;color:var(--ink);position:relative}

  .spread{position:absolute;left:40px;top:252px;width:720px;height:360px;display:flex;box-shadow:0 6px 24px rgba(0,0,0,.12)}
  .page{position:relative;width:360px;height:360px;overflow:hidden}
  .page--inner-left{background:var(--page-tint)}
  .page--inner-right{background:var(--page-white)}
  .cover{position:absolute;left:800px;top:252px;width:360px;height:360px;overflow:hidden;box-shadow:0 6px 24px rgba(0,0,0,.12)}

  .dots{position:absolute;left:34px;top:30px;display:flex;gap:5px}
  .dots span{width:5px;height:5px;border-radius:50%;background:var(--ink)}

  .body-copy{font-size:7px;line-height:1.45;color:var(--ink)}
  .body-copy p{margin-bottom:7px}
  .body-copy strong{font-weight:800}
  .intro{position:absolute;left:34px;top:92px;width:212px}

  .photo-blob{position:absolute;left:232px;top:40px;width:128px;height:140px}
  .arc{position:absolute;left:0;top:0;width:720px;height:360px;pointer-events:none}

  .pill-heading{display:inline-block;background:var(--pill);border-radius:20px;padding:4px 14px 3px;font-weight:800;font-size:15px;letter-spacing:.06em;color:var(--ink);font-stretch:125%}
  .right-head{position:absolute;left:28px;top:30px}
  .question-list{position:absolute;left:28px;top:64px;width:310px;list-style:none;font-size:6.6px;line-height:1.5}
  .question-list li{text-indent:-8px;padding-left:8px}
  .question-list strong{font-weight:800}
  .closing{position:absolute;left:28px;top:196px;width:304px;font-size:6.6px}

  .cover-photo{position:absolute;inset:0;background:
     radial-gradient(ellipse 42% 55% at 48% 62%, #f0d3c6 0%, #e6bfae 45%, rgba(230,191,174,0) 75%),
     radial-gradient(ellipse 60% 40% at 70% 95%, #b98a74 0%, rgba(185,138,116,0) 70%),
     linear-gradient(160deg,#8d96a8 0%,#b3bac7 35%,#c9ccd3 55%,#9b8f8c 100%)}
  .cover-title{position:absolute;left:26px;top:30px;display:flex;flex-direction:column;align-items:flex-start;gap:4px}
  .cover-title .pill-heading{background:rgba(240,240,246,.92);font-size:17px;padding:4px 12px 3px}
  .cover-sub{position:absolute;left:30px;top:98px;width:230px;font-size:7.6px;line-height:1.4;color:#eef0fa}
  .brand{position:absolute;right:26px;bottom:22px;display:flex;align-items:center;gap:6px;font-size:9px;font-weight:600;color:#ffffff}
  .brand .mark{width:9px;height:9px;border-radius:50%;background:#ffffff}
</style>
</head>
<body>

<section class="spread" aria-label="Innenseiten des Flyers">
  <div class="page page--inner-left">
    <div class="dots"><span></span><span></span><span></span></div>

    <div class="body-copy intro">
      <p><strong>Mutter sein ist wunderbar.</strong> Wenn eine Frau Mutter wird, ist sie plötzlich verliebt über beide Ohren, unbändig stolz und von Glücksgefühlen völlig überwältigt. So ist es doch <strong>NORMAL, oder...?</strong></p>
      <p><strong>Überforderung, Frustration</strong> und <strong>Verzweiflung</strong> kennen Mütter, Frauen mit Kinderwunsch und werdende Mütter allerdings ebenfalls nur zu gut. Wichtig ist, dass die Beurteilung einer Situation, d.h. wie stark sie uns belastet alleine uns selbst zusteht. Nur unsere eigene <strong>subjektive Einschätzung</strong> ist ausschlaggebend.</p>
      <p>So unterschiedlich wir Menschen sind, so verschieden ist auch unser persönliches Fühlen und Erleben. Deshalb benötigen wir <strong>individuell passende Lösungen</strong> für unsere Herausforderungen.</p>
    </div>

    <svg class="photo-blob" viewBox="0 0 128 140" role="img" aria-label="Foto: Mutter mit Kind auf dem Arm vor hellem Himmel, von hinten">
      <defs>
        <linearGradient id="blobFill" x1="0" y1="0" x2="0.6" y2="1">
          <stop offset="0" stop-color="var(--photo-sky)"/>
          <stop offset="0.55" stop-color="#b9c7d2"/>
          <stop offset="1" stop-color="var(--photo-hair)"/>
        </linearGradient>
      </defs>
      <path d="M20 18 C45 0 100 4 118 30 C128 60 120 110 90 132 C60 146 18 126 8 92 C0 62 2 32 20 18 Z" fill="url(#blobFill)"/>
    </svg>
  </div>

  <div class="page page--inner-right">
    <div class="right-head"><span class="pill-heading">WENN ALSO...</span></div>
    <ul class="question-list">
      <li>... wir <strong>gern Mutter wären</strong> aber das Leben andere Pläne hat?</li>
      <li>... uns die Erfahrung der <strong>Geburt belastet</strong>, aber niemand zuhört weil ja „jetzt alles ok ist“?</li>
      <li>... wenn wir unser <strong>Kind verloren</strong> haben?</li>
      <li>... unser Kind oder wir selbst mit einer <strong>Krankheit</strong> zu kämpfen haben?</li>
      <li>... wir selbst oder unser Partner uns <strong>kaum wiedererkennen?</strong></li>
      <li>... wir uns das vielleicht so gar nicht vorgestellt hatten und jetzt nicht nur voller Glückseligkeit herumwandeln?</li>
      <li>... wir eben <strong>nicht stolz</strong> darauf sind wie wir den letzten Schreianfall unseres Babys begleitet haben?</li>
      <li>... wir weder die Wut unseres Kindes, noch unsere eigene <strong>Wut</strong> gebändigt bekommen?</li>
      <li>... wir mit der Situation <strong>überfordert</strong> sind und nicht mehr weiter wissen?</li>
    </ul>
    <div class="body-copy closing">
      <p>Ja, Mutter sein ist wundervoll! Und ja, die Dynamik der Paarbeziehung bricht zusammen und wir stehen plötzlich vor einer der erfüllendsten Aufgaben und zugleich einer der größten <strong>existentiellen Herausforderungen</strong> die uns das Leben bietet: <strong>Eltern sein.</strong></p>
      <p>Um trotz Rückschlägen ein zufriedenes Leben zu führen und um feinfühlig für unsere Kinder da zu sein, benötigen wir viel Kraft. Mentale Kraft, die es uns ermöglicht aus den Augen unserer Kinder zu sehen, unsere eigenen Gefühle zu regulieren und die starken Gefühle unserer Kinder auszuhalten und zu begleiten.</p>
      <p>Gemeinsam erarbeiten wir <strong>individuelle Strategien,</strong> wie Sie auf Ihre eigenen Ressourcen besser zugreifen, und so mental gestärkt nach vorne schauen können.</p>
    </div>
  </div>

  <svg class="arc" viewBox="0 0 720 360" aria-hidden="true">
    <path d="M300 38 C316 60 318 100 306 140" fill="none" stroke="var(--ink)" stroke-width="1.4"/>
    <path d="M322 182 C345 205 385 205 400 178" fill="none" stroke="var(--ink)" stroke-width="1.4"/>
  </svg>
</section>

<section class="cover" aria-label="Titelseite des Flyers">
  <div class="cover-photo" role="img" aria-label="Foto: Babyfuß in der Hand einer Erwachsenen, weich unscharfer Hintergrund"></div>
  <div class="cover-title">
    <span class="pill-heading">KRISENBEGLEITUNG</span>
    <span class="pill-heading">UND LEBENSBERATUNG</span>
  </div>
  <p class="cover-sub">Psychologische Beratungspraxis für Mütter, Schwangere und Frauen mit Kinderwunsch</p>
  <div class="brand"><span class="mark"></span>Gelassenheitswerkstatt</div>
</section>

</body>
</html>
```